South Carolina Bridal and Formal Wear Store

We want The Gown Parlor of Ashcombe website to feel luxurious, elegant, welcoming, and approachable—without feeling overpriced or intimidating. The site should immediately show that we are a full-service bridal and formal wear destination, offering bridal gowns, prom, mothers’ dresses, tuxedos and suits, accessories, and more. We want beautiful, high-end imagery and a clean, modern design while still reflecting the warm, personal experience customers receive when they walk into our boutique. Most importantly, the website should be easy to shop and navigate, allowing customers to browse our collections, see what we offer, understand price ranges, book appointments, and feel excited and comfortable choosing The Gown Parlor of Ashcombe for all of their special-event needs.

Target Market(s)

Women ages 18-50. Brides, engaged women, mothers of the occasion

Industry/Entity Type

Bridal and Formal Wear

Coding

Coded - Design and coding required

Number of Pages Required

5+ page

Font styles to use
Sans Serif

Colors

Designer to choose colors to be used in the design.

Requirements
Must have
• Appointment area, about us staff area, what we offer and designers our logo
Nice to have
• Modern Southern Luxury: Clean, elegant, and upscale with soft neutral tones, beautiful bridal photography, and a warm Lowcountry feel.
Should not have
• pricing

```html
<!DOCTYPE html>
<html lang="en">
<head>
<meta charset="utf-8">
<title>The Gown Parlor of Ashcombe — Website Concept</title>
<link href="https://fonts.googleapis.com/css2?family=Montserrat:wght@400;500;600&family=Lato:wght@400;700&family=Pinyon+Script&display=swap" rel="stylesheet">
<style>
:root{
  --ivory:#f8f5ef; --pearl:#f1ece3; --sand:#e3d4bb; --champagne:#d7b88c;
  --taupe:#c0a994; --charcoal:#2a2a2a; --sage:#8b9a6c; --olive:#6d6b4e;
  --board:#f4f1ea; --text:#3b3631; --muted:#7c746b; --line:#d9d1c4;
  --wood:#5a4330; --wood-dark:#3e2e22; --lawn:#6f7a4c; --marsh:#8a8670;
}
*{box-sizing:border-box;margin:0;padding:0}
html,body{width:1200px;height:849px;overflow:hidden;background:var(--board)}
body{position:relative;font-family:'Lato',sans-serif;color:var(--text)}
.abs{position:absolute}
.sans{font-family:'Montserrat',sans-serif}
.photo{position:absolute}

/* left column */
.brand-box{left:13px;top:13px;width:199px;height:72px;background:#111;color:#fff;display:flex;flex-direction:column;align-items:center;justify-content:center;font-family:'Montserrat',sans-serif;font-weight:500;letter-spacing:1px}
.brand-box .name{font-size:15px;letter-spacing:.5px}
.brand-box .sub{font-size:7px;letter-spacing:2px;margin-top:5px}
.intro-title{left:18px;top:112px;font-family:'Montserrat',sans-serif;font-size:11.5px;letter-spacing:1px}
.intro-script{left:20px;top:136px;font-family:'Pinyon Script',cursive;font-size:13px;color:#8b7d62;white-space:nowrap}
.intro-copy{left:18px;top:165px;width:185px;font-size:7.6px;line-height:13px;color:#4b443d}
.divider{left:22px;top:242px;width:170px;height:1px;background:var(--line)}
.divider::after{content:"";position:absolute;left:80px;top:-4px;width:8px;height:8px;border:1px solid var(--taupe);border-radius:50%;background:var(--board)}
.features{left:18px;top:260px;list-style:none}
.features li{display:flex;align-items:center;gap:10px;height:23px;font-family:'Montserrat',sans-serif;font-size:7.8px;letter-spacing:.6px}
.features li span.ic{width:10px;height:10px;border:1px solid var(--taupe);border-radius:50%}
.left-photo{left:0;top:356px;width:220px;height:316px;background:linear-gradient(180deg,rgba(244,241,234,1) 0%,#c6c8b5 10%,#8d9870 40%,#6a7b44 72%,#5c6e3a 100%)}
.palette-label{left:84px;top:684px;font-family:'Montserrat',sans-serif;font-size:6.5px;font-weight:600;letter-spacing:.6px}
.swatches{left:8px;top:698px;display:flex;gap:6px}
.swatch{width:24px;display:flex;flex-direction:column;align-items:center;font-size:4px;letter-spacing:0;font-family:'Montserrat',sans-serif;white-space:nowrap}
.swatch i{display:block;width:24px;height:20px;margin-bottom:6px;border:1px solid #e3ddd2}
.type-label{left:87px;top:745px;font-family:'Montserrat',sans-serif;font-size:6.5px;font-weight:600;letter-spacing:.6px}
.type-spec{font-size:5px;letter-spacing:.4px;font-family:'Montserrat',sans-serif;white-space:nowrap}
.type-spec b{display:block;font-size:7px;font-weight:500;margin-top:6px}
.type-aa{font-size:16px}
.leaf{left:0;top:790px;width:70px;height:59px;background:radial-gradient(ellipse at 20% 80%,#a7b08c 0%,rgba(167,176,140,0) 70%)}

/* page mockups */
.page-label{font-family:'Montserrat',sans-serif;font-size:7.5px;font-weight:600;letter-spacing:.5px}
.mock{position:absolute;background:var(--ivory);box-shadow:0 1px 4px rgba(0,0,0,.18);overflow:hidden}
.nav{position:absolute;left:0;top:0;right:0;background:#fff;display:flex;align-items:center;justify-content:space-between;padding:0 8px}
.nav .logo{font-family:'Montserrat',sans-serif;font-weight:500;color:var(--charcoal);line-height:1}
.nav .logo small{display:block;font-size:.45em;letter-spacing:1px;margin-top:2px}
.nav ul{display:flex;list-style:none;font-family:'Montserrat',sans-serif;color:#555}
.hero{position:absolute;left:0;right:0}
.hero-text{position:absolute;color:#fff;font-family:'Montserrat',sans-serif}
.btn{display:inline-block;font-family:'Montserrat',sans-serif;letter-spacing:.4px;text-align:center}
.btn-light{background:#f6f1e8;color:var(--text)}
.btn-outline{border:1px solid var(--taupe);color:var(--text)}
.btn-sand{background:var(--champagne);color:var(--text);border:1px solid #b99c72}
.center{position:absolute;left:0;right:0;text-align:center;font-family:'Montserrat',sans-serif}
.tabs{display:flex;justify-content:center;gap:12px;font-size:4px;letter-spacing:.3px;color:#555}
.tabs span:first-child{border-bottom:1px solid #999}
.band{position:absolute;left:0;right:0;color:#fff;text-align:center;font-family:'Montserrat',sans-serif}

/* home */
.home{left:233px;top:38px;width:395px;height:790px}
.home .nav{height:41px;font-size:4.5px}
.home .nav .logo{font-size:10px}
.home .nav ul{gap:9px}
.home .hero{top:41px;height:200px;background:linear-gradient(100deg,var(--wood-dark) 0%,#6b5039 45%,#a89684 70%,#7a5e45 100%)}
.welcome-title{position:absolute;left:22px;top:287px;font-family:'Montserrat',sans-serif;font-size:5.6px;letter-spacing:.4px;white-space:nowrap}
.welcome-copy{position:absolute;left:22px;top:302px;width:162px;font-size:5.2px;line-height:9px}
.offer-tile{position:absolute;top:430px;width:53px;height:88px}
.offer-cap{position:absolute;top:525px;width:59px;text-align:center;font-family:'Montserrat',sans-serif;font-size:4.6px;letter-spacing:.2px}
.offer-cap small{display:block;font-size:3.8px;color:var(--muted);margin-top:3px}
.promise{position:absolute;top:662px;width:80px;text-align:center;font-family:'Montserrat',sans-serif;font-size:5px;letter-spacing:.4px;line-height:8px}
.promise i{display:block;width:18px;height:18px;margin:0 auto 6px;border:1px solid var(--taupe);border-radius:50%}
.footer{position:absolute;left:0;right:0;top:722px;height:68px;background:var(--olive);color:#f2ede2}
.social{position:absolute;top:30px;width:9px;height:9px;border-radius:50%;background:#f2ede2}

/* secondary pages */
.sub-page .nav{height:28px;font-size:3px}
.sub-page .nav .logo{font-size:7px}
.sub-page .nav ul{gap:5px}
.sub-page .hero-text h2{font-size:10px;font-weight:500;letter-spacing:.6px}
.sub-page .hero-text p{font-size:4.5px;margin:4px 0 7px;opacity:.9}
.sub-page .btn-light{font-size:3.4px;padding:2px 7px}
.grid-photo{position:absolute;top:0;width:75px;height:103px}
.view-btn{position:absolute;left:50%;transform:translateX(-50%);font-size:3.4px;padding:2px 7px;background:#fff;border:1px solid var(--line);font-family:'Montserrat',sans-serif;white-space:nowrap}

.designer-grid{position:absolute;left:13px;top:174px;width:243px;display:grid;grid-template-columns:repeat(3,1fr);gap:2px}
.designer-grid div{height:48px;background:#ede7dc;display:flex;flex-direction:column;align-items:center;justify-content:center;font-family:'Montserrat',sans-serif;font-size:8px;letter-spacing:.8px;color:#3d3833;text-align:center;line-height:1}
.designer-grid small{font-size:3.5px;letter-spacing:.5px;margin-top:2px}
</style>
</head>
<body>

<!-- Left presentation column -->
<div class="abs brand-box"><span class="name">The Gown Parlor</span><span class="sub">OF ASHCOMBE</span><span class="sub" style="margin-top:4px;font-size:6px">BRIDAL · TUXEDOS · FORMAL WEAR</span></div>
<div class="abs intro-title">A NEW DIGITAL EXPERIENCE</div>
<div class="abs intro-script">Rooted in Ashcombe. Made for You.</div>
<p class="abs intro-copy">A refined, elegant website designed to showcase The Gown Parlor of Ashcombe’s curated collections, trusted expertise, and unforgettable experience for every milestone.</p>
<div class="abs divider"></div>
<ul class="abs features">
  <li><span class="ic"></span>ELEGANT &amp; INVITING</li>
  <li><span class="ic" style="border-radius:1px"></span>EASY TO BROWSE</li>
  <li><span class="ic"></span>DESIGNED FOR EVERY MILESTONE</li>
  <li><span class="ic"></span>ROOTED IN THE LOWCOUNTRY</li>
</ul>
<div class="photo left-photo" role="img" aria-label="Bride in a strapless ivory gown holding a white bouquet on a green lawn"></div>

<div class="abs palette-label">COLOR PALETTE</div>
<div class="abs swatches">
  <div class="swatch"><i style="background:var(--ivory)"></i>IVORY</div>
  <div class="swatch"><i style="background:var(--pearl)"></i>PEARL</div>
  <div class="swatch"><i style="background:var(--sand)"></i>SAND</div>
  <div class="swatch"><i style="background:var(--champagne)"></i>CHAMPAGNE</div>
  <div class="swatch"><i style="background:var(--taupe)"></i>TAUPE</div>
  <div class="swatch"><i style="background:var(--charcoal)"></i>CHARCOAL</div>
  <div class="swatch"><i style="background:var(--sage)"></i>SAGE</div>
</div>
<div class="abs type-label">TYPOGRAPHY</div>
<div class="abs type-spec" style="left:18px;top:765px">HEADING FONT<b>MONTSERRAT</b></div>
<div class="abs type-aa sans" style="left:88px;top:768px">Aa</div>
<div class="abs type-spec" style="left:134px;top:765px">BODY FONT<b style="font-family:'Lato',sans-serif">LATO</b></div>
<div class="abs type-aa" style="left:180px;top:768px">Aa</div>
<div class="abs leaf" role="img" aria-label="Soft sage foliage accent"></div>

<!-- 1. Home -->
<div class="abs page-label" style="left:236px;top:20px">1.&nbsp; HOME</div>
<div class="mock home">
  <div class="nav">
    <div class="logo">The Gown Parlor<small>OF ASHCOMBE</small></div>
    <ul><li style="color:var(--champagne)">HOME</li><li>BRIDAL ▾</li><li>PROM</li><li>MOTHERS</li><li>TUXEDOS</li><li>DESIGNERS</li><li>ABOUT</li><li>APPOINTMENT</li><li>CONTACT</li></ul>
  </div>
  <div class="hero" role="img" aria-label="Bride in a corseted satin ball gown in a historic wood-panelled doorway"></div>
  <div class="hero-text" style="left:21px;top:96px">
    <div style="font-size:14.5px;letter-spacing:.8px;line-height:21px">SAY YES TO<br>THE ONE</div>
    <div style="font-size:6px;letter-spacing:.6px;line-height:10px;margin-top:12px">BEAUTIFUL BEGINNINGS<br>START HERE.</div>
    <span class="btn btn-light" style="font-size:4.8px;padding:5px 11px;margin-top:14px">BOOK APPOINTMENT</span>
  </div>
  <div class="welcome-title">WELCOME TO THE GOWN PARLOR OF ASHCOMBE</div>
  <p class="welcome-copy">Your destination for bridal gowns, prom, mothers’ dresses, tuxedos &amp; suits, and accessories. Experience personalized service in a warm, relaxed setting—where every detail is chosen with you in mind.</p>
  <span class="abs btn btn-outline" style="left:22px;top:350px;font-size:4.5px;padding:3px 9px">OUR PROMISE</span>
  <div class="photo" style="left:196px;top:257px;width:168px;height:129px;background:linear-gradient(180deg,#51583a 0%,#6f7a4b 50%,#8d9a5c 100%)" role="img" aria-label="Bride walking beneath live oak trees"></div>

  <div class="center" style="top:408px;font-size:9px;letter-spacing:.8px">WHAT WE OFFER</div>
  <div class="offer-tile" style="left:21px;background:linear-gradient(#b5a48d,#e8e0d1)" role="img" aria-label="Bridal gown"></div>
  <div class="offer-tile" style="left:80px;background:linear-gradient(#a58b78,#d5a79b)" role="img" aria-label="Blush prom gown"></div>
  <div class="offer-tile" style="left:139px;background:linear-gradient(#8a847b,#6b6a72)" role="img" aria-label="Mother’s dress in pewter"></div>
  <div class="offer-tile" style="left:198px;background:linear-gradient(#b8ad9b,#2a2a2a 60%)" role="img" aria-label="Black tuxedo"></div>
  <div class="offer-tile" style="left:257px;background:linear-gradient(#c7ad88,#8a6e4e)" role="img" aria-label="Accessories and florals"></div>
  <div class="offer-tile" style="left:316px;background:linear-gradient(#96a2a6,#ece6dc)" role="img" aria-label="Bride by the water"></div>
  <div class="offer-cap" style="left:18px">BRIDAL GOWNS<small>Find Your Gown</small></div>
  <div class="offer-cap" style="left:77px">PROM &amp; FORMAL<small>Make It Unforgettable</small></div>
  <div class="offer-cap" style="left:136px">MOTHERS’ DRESSES<small>Celebrate in Style</small></div>
  <div class="offer-cap" style="left:195px">TUXEDOS &amp; SUITS<small>Look Your Best</small></div>
  <div class="offer-cap" style="left:254px">ACCESSORIES<small>The Finishing Touch</small></div>
  <div class="offer-cap" style="left:313px">AND MORE<small>Everything You Need</small></div>

  <div class="band" style="top:571px;height:79px;background:linear-gradient(180deg,#8e8676,#6e6a56 60%,#5a5842)" role="img" aria-label="Lowcountry marsh at dusk">
    <div style="font-size:5.5px;letter-spacing:.6px;margin-top:13px">PROUDLY SERVING ASHCOMBE &amp; THE LOWCOUNTRY</div>
    <div style="font-family:'Lato',sans-serif;font-size:5.5px;margin-top:8px">A boutique experience with Southern heart.</div>
    <span class="btn btn-light" style="font-size:4.5px;padding:4px 11px;margin-top:8px">BOOK YOUR APPOINTMENT</span>
  </div>

  <div class="promise" style="left:18px"><i></i>PERSONALIZED<br>EXPERIENCE</div>
  <div class="promise" style="left:113px"><i></i>CURATED<br>COLLECTIONS</div>
  <div class="promise" style="left:203px"><i></i>EXPERT<br>STYLING</div>
  <div class="promise" style="left:292px"><i></i>MEMORABLE<br>MOMENTS</div>

  <div class="footer">
    <div class="abs" style="left:15px;top:24px;font-family:'Montserrat',sans-serif;font-size:9px;line-height:1">The Gown Parlor<div style="font-size:4px;letter-spacing:1px;margin-top:3px">OF ASHCOMBE · BRIDAL · FORMAL WEAR</div></div>
    <div class="center" style="top:30px;font-size:4.8px;letter-spacing:.5px;line-height:11px">ASHCOMBE, SOUTH CAROLINA<br>WHERE BEAUTIFUL BEGINNINGS BEGIN</div>
    <span class="social" style="left:330px"></span><span class="social" style="left:345px"></span><span class="social" style="left:360px"></span>
  </div>
</div>

<!-- 2. Bridal Gowns -->
<div class="abs page-label" style="left:645px;top:20px">2.&nbsp; BRIDAL GOWNS</div>
<div class="mock sub-page" style="left:638px;top:38px;width:264px;height:359px">
  <div class="nav"><div class="logo">The Gown Parlor<small>OF ASHCOMBE</small></div><ul><li>HOME</li><li>BRIDAL</li><li>PROM</li><li>MOTHERS</li><li>TUXEDOS</li><li>DESIGNERS</li><li>ABOUT</li><li>APPOINTMENT</li><li>CONTACT</li></ul></div>
  <div class="hero" style="top:28px;height:100px;background:linear-gradient(100deg,#4a3727,#7a5c42 55%,#bfb2a0 75%,#6e533c)" role="img" aria-label="Bride in a corseted gown in an ornate interior"></div>
  <div class="hero-text" style="left:25px;top:62px"><h2>BRIDAL GOWNS</h2><p>Timeless. Elegant. Uniquely You.</p><span class="btn btn-light">BOOK APPOINTMENT</span></div>
  <div class="center" style="top:139px;font-size:6.5px;letter-spacing:.5px">OUR COLLECTIONS</div>
  <div class="center" style="top:151px;font-family:'Lato',sans-serif;font-size:4px;color:var(--muted)">Curated gowns for every bride, every style, every story.</div>
  <div class="center tabs" style="top:162px"><span>ALL STYLES</span><span>CLASSIC</span><span>MODERN</span><span>ROMANTIC</span><span>MINIMALIST</span></div>
  <div class="abs" style="left:14px;top:175px">
    <div class="grid-photo" style="left:0;background:linear-gradient(#6b5240,#e6dfd3)" role="img" aria-label="Satin ball gown"></div>
    <div class="grid-photo" style="left:80px;background:linear-gradient(#8a7a66,#efe9df)" role="img" aria-label="Strapless fitted mermaid gown"></div>
    <div class="grid-photo" style="left:160px;background:linear-gradient(#7d6a59,#e9e0d2)" role="img" aria-label="Lace ball gown"></div>
  </div>
  <div class="view-btn" style="top:290px">VIEW ALL BRIDAL GOWNS</div>
  <div class="band" style="top:304px;height:55px;background:linear-gradient(180deg,#8a8572,#5d5a45)" role="img" aria-label="Lowcountry waterfront">
    <div style="font-size:5.2px;letter-spacing:.5px;margin-top:11px;line-height:8px">YOUR DRESS. YOUR MOMENT.<br>WE’LL MAKE IT UNFORGETTABLE.</div>
    <span class="btn btn-light" style="font-size:3.4px;padding:2px 7px;margin-top:4px">BOOK YOUR APPOINTMENT</span>
  </div>
</div>

<!-- 3. Prom & Formal -->
<div class="abs page-label" style="left:918px;top:20px">3.&nbsp; PROM &amp; FORMAL</div>
<div class="mock sub-page" style="left:911px;top:38px;width:271px;height:359px">
  <div class="nav"><div class="logo">The Gown Parlor<small>OF ASHCOMBE</small></div><ul><li>HOME</li><li>BRIDAL</li><li>PROM</li><li>MOTHERS</li><li>TUXEDOS</li><li>DESIGNERS</li><li>ABOUT</li><li>APPOINTMENT</li><li>CONTACT</li></ul></div>
  <div class="hero" style="top:28px;height:100px;background:linear-gradient(100deg,#3d2c20,#5d4433 55%,#2f4a3a 72%,#4d3a2a)" role="img" aria-label="Woman in an emerald satin gown in a grand hall"></div>
  <div class="hero-text" style="left:23px;top:62px"><h2>PROM &amp; FORMAL</h2><p>Make It Your Moment.</p><span class="btn btn-light">BOOK APPOINTMENT</span></div>
  <div class="center" style="top:139px;font-size:6.5px;letter-spacing:.5px">STYLES THAT SHINE</div>
  <div class="center" style="top:151px;font-family:'Lato',sans-serif;font-size:4px;color:var(--muted)">Dresses that turn heads and create memories.</div>
  <div class="center tabs" style="top:162px"><span>ALL</span><span>LONG</span><span>SHORT</span><span>GLAM</span><span>TRENDING</span></div>
  <div class="abs" style="left:16px;top:175px">
    <div class="grid-photo" style="left:0;width:77px;background:linear-gradient(#6b5a4a,#2c3e66)" role="img" aria-label="Navy sequin gown"></div>
    <div class="grid-photo" style="left:81px;width:77px;background:linear-gradient(#8b7868,#e0a4ad)" role="img" aria-label="Blush pink gown"></div>
    <div class="grid-photo" style="left:162px;width:77px;background:linear-gradient(#6b5a4a,#1f4a36)" role="img" aria-label="Emerald satin gown"></div>
  </div>
  <div class="view-btn" style="top:297px">VIEW ALL PROM &amp; FORMAL</div>
  <div class="band" style="top:318px;height:41px;background:linear-gradient(180deg,#958b73,#6a634a)" role="img" aria-label="Palmetto-lined marsh">
    <div style="font-size:5.2px;letter-spacing:.5px;margin-top:11px">FIND THE ONE THAT MAKES YOU FEEL AMAZING.</div>
    <span class="btn btn-light" style="font-size:3.4px;padding:2px 7px;margin-top:5px">BOOK APPOINTMENT</span>
  </div>
</div>

<!-- 4. Tuxedos & Suits -->
<div class="abs page-label" style="left:645px;top:408px">4.&nbsp; TUXEDOS &amp; SUITS</div>
<div class="mock sub-page" style="left:638px;top:421px;width:264px;height:382px">
  <div class="nav"><div class="logo">The Gown Parlor<small>OF ASHCOMBE</small></div><ul><li>HOME</li><li>BRIDAL</li><li>PROM</li><li>MOTHERS</li><li>TUXEDOS</li><li>DESIGNERS</li><li>ABOUT</li><li>APPOINTMENT</li><li>CONTACT</li></ul></div>
  <div class="hero" style="top:27px;height:101px;background:linear-gradient(100deg,#2e3a2e,#55584a 45%,#e2ddd2 62%,#222 80%,#cfc8bb)" role="img" aria-label="Groom in a black tuxedo on a plantation-style porch"></div>
  <div class="hero-text" style="left:20px;top:62px"><h2>TUXEDOS &amp; SUITS</h2><p>Sharp Looks. Confident You.</p><span class="btn btn-light">BOOK APPOINTMENT</span></div>
  <div class="center" style="top:140px;font-size:6px;letter-spacing:.5px">LOOK YOUR BEST FOR EVERY OCCASION</div>
  <div class="center" style="top:152px;font-family:'Lato',sans-serif;font-size:4px;color:var(--muted)">From classic to modern, we have the perfect look.</div>
  <div class="center tabs" style="top:163px"><span>ALL STYLES</span><span>CLASSIC</span><span>MODERN</span><span>SLIM FIT</span><span>TRENDING</span></div>
  <div class="abs" style="left:14px;top:180px">
    <div class="grid-photo" style="left:0;background:linear-gradient(#d9d2c4,#1f2a44 55%)" role="img" aria-label="Navy tuxedo"></div>
    <div class="grid-photo" style="left:80px;background:linear-gradient(#e4ded2,#1d1d1d 55%)" role="img" aria-label="Black tuxedo"></div>
    <div class="grid-photo" style="left:160px;background:linear-gradient(#c9bfae,#2d2d2d 55%)" role="img" aria-label="Charcoal tuxedo"></div>
  </div>
  <div class="view-btn" style="top:291px">VIEW ALL TUXEDOS &amp; SUITS</div>
  <div class="band" style="top:315px;height:67px;background:linear-gradient(180deg,#85806c,#55523e)" role="img" aria-label="Marsh with live oaks">
    <div style="font-size:5.5px;letter-spacing:.5px;margin-top:15px">SCHEDULE YOUR APPOINTMENT</div>
    <div style="font-family:'Lato',sans-serif;font-size:4px;margin-top:2px">We can’t wait to welcome you.</div>
    <span class="btn btn-light" style="font-size:3.4px;padding:2px 7px;margin-top:4px">BOOK YOUR APPOINTMENT</span>
  </div>
</div>

<!-- 5. Designers -->
<div class="abs page-label" style="left:915px;top:408px">5.&nbsp; DESIGNERS</div>
<div class="mock sub-page" style="left:911px;top:421px;width:273px;height:382px">
  <div class="nav"><div class="logo">The Gown Parlor<small>OF ASHCOMBE</small></div><ul><li>HOME</li><li>BRIDAL</li><li>PROM</li><li>MOTHERS</li><li>TUXEDOS</li><li>DESIGNERS</li><li>ABOUT</li><li>APPOINTMENT</li><li>CONTACT</li></ul></div>
  <div class="hero" style="top:27px;height:105px;background:linear-gradient(100deg,#3e4228,#5f6a3c 45%,#8c9360 65%,#4a5230)" role="img" aria-label="Smiling bride in a strapless gown amid garden greenery"></div>
  <div class="hero-text" style="left:26px;top:64px"><h2>OUR DESIGNERS</h2><p>Handpicked. Trusted. Loved.</p></div>
  <div class="center" style="top:141px;font-size:6px;letter-spacing:.5px;line-height:9px">WE PARTNER WITH THE WORLD’S<br>MOST BELOVED DESIGNERS</div>
  <div class="center" style="top:163px;font-family:'Lato',sans-serif;font-size:4px;color:var(--muted)">Bringing you exceptional quality, craftsmanship, and style.</div>
  <div class="designer-grid">
    <div>VERITY<small>&amp; LANE</small></div>
    <div>ODILE<small>MARCHAND</small></div>
    <div>LUMEN<small>OF SYDNEY</small></div>
    <div>HAVENROSE<small>CLARA WELLS</small></div>
    <div>CALLA<small>BRIDALS</small></div>
    <div>SERAPHINE<small>VALE</small></div>
    <div><small style="margin:0 0 2px">THEO</small>ARDLEY</div>
    <div>J4<small>MARLOWE</small></div>
    <div>WHITCOMB<small>and more</small></div>
  </div>
  <div class="center" style="top:334px;font-family:'Lato',sans-serif;font-size:4.5px;color:var(--muted)">Our collections are always evolving—visit us to see what’s new!</div>
  <div class="center" style="top:351px"><span class="btn btn-sand" style="font-size:4.5px;padding:4px 11px">BOOK AN APPOINTMENT</span></div>
</div>

</body>
</html>
```